VerdaTurf - 11" x 4" Door Hanger, full color both sides

We need a door hanger designed, 11" x 4", full color both sides, We are a lawn care company that provides lawn mowing, and other services to clients. This door hanger will be place on the 9 neighbors of our current clients. The ad needs to state that we provided lawn service to one of their neighbors today, and that we are in their neighborhood each week on that day. The door hanger will have 4 printings, substituting the day of Tuesday, Wednesday, Thursday, and Friday. All the art work and text will remain the same except the day of the week. For information about VerdaTurf, please visit our website www.verdaturf-example.net. The main emphasis of the message should be that we are their every week on that day, and the benefits to them of using our service (ie. quality time with their family, golf, sports, resting, etc., instead of mowing the lawn). At the bottom of the door hanger will be a coupon offering their tenth (10th) lawn service free, which is the same as a 10% discount.

I have uploaded a template files for the front and back of an 11 x 4 door hanger, The templates are pdf, jpeg, or eps files. The final product can be a pdf, jpeg, or eps file.

Target Market(s)

Neighbors of our existing clients

Industry/Entity Type

Lawn Care

Font styles to use
Serif

Requirements
Must have
• Professional design and art, Short conversational message that relays the following thoughts:
• 1. We mowed your neighbor's lawn today!
• 2. We are in your neighborhood every Tuesday!
• 3. Our lawn service is guaranteed.
• 4. Call to action - Call us today! 512-748-3091
• 5. Of course our contact info, name, phone number, website address.
• 6. Coupon at bottom for "10th lawn service Free!"
Nice to have
• Art work from our website is fine to use, That carries our theme throughout our campaign.
Should not have
• Very wordy. This is basically a billboard, Have very few seconds to grab their attention.

```html
<!DOCTYPE html>
<html lang="en">
<head>
<meta charset="utf-8">
<title>VerdaTurf Door Hanger</title>
<link href="https://fonts.googleapis.com/css2?family=Crimson+Pro:wght@400;600;700&family=Montserrat:wght@600;700&display=swap" rel="stylesheet">
<style>
  :root {
    --bg: #ece6dc;
    --green-deep: #137a3e;
    --green-mid: #2f9a45;
    --green-light: #72b244;
    --photo-dark: #1f4a26;
    --photo-mid: #3f7d34;
    --white: #ffffff;
    --red: #e0252f;
    --ink: #222222;
  }
  * { margin: 0; padding: 0; box-sizing: border-box; }
  html, body { width: 1200px; height: 1200px; overflow: hidden; }
  body { background: var(--bg); position: relative; font-family: "Crimson Pro", Georgia, serif; }

  .hanger {
    position: absolute; top: 80px; width: 370px; height: 1018px;
    border-radius: 18px; overflow: hidden; background: var(--white);
    box-shadow: 0 4px 14px rgba(0,0,0,.18);
  }
  .hanger--front { left: 196px; }
  .hanger--back { left: 613px; }

  .panel {
    position: absolute; left: 0; top: 0; width: 100%; height: 888px;
    background: linear-gradient(180deg, var(--green-deep) 0%, var(--green-mid) 55%, var(--green-light) 100%);
  }
  .hanger--back .panel {
    background: linear-gradient(180deg, var(--green-deep) 30%, #1a8a3e 70%, var(--green-light) 100%);
  }
  .photo { position: absolute; left: 0; top: 0; width: 100%; }
  .photo--family {
    height: 500px;
    background: linear-gradient(180deg, var(--photo-dark) 0%, #2f6a2c 45%, #4a9a36 75%, rgba(76,160,60,0) 100%);
  }
  .photo--lawn {
    height: 320px;
    background: linear-gradient(180deg, #0f3a1c 0%, #3d8a34 45%, #5aa23f 70%, rgba(26,138,62,0) 100%);
  }
  .hole {
    position: absolute; left: 137px; top: 106px; width: 96px; height: 96px;
    border-radius: 50%; background: var(--bg);
  }

  .center { position: absolute; left: 0; width: 100%; text-align: center; color: var(--white); }
  .headline { font-size: 27px; line-height: 26px; }
  .msg-1 { top: 428px; }
  .msg-2 { top: 530px; }
  .msg-3 { top: 633px; }

  .cta {
    position: absolute; left: 33px; top: 719px; width: 305px; height: 35px;
    border: 2px solid var(--white); color: var(--white);
    font-family: "Montserrat", Arial, sans-serif; font-weight: 700; font-size: 17px;
    display: flex; align-items: center; justify-content: center;
  }
  .contact { top: 778px; font-size: 15px; line-height: 18px; }
  .contact .name, .contact .web { font-weight: 700; }

  .tearline {
    position: absolute; left: 0; top: 888px; width: 100%;
    border-top: 2px dashed var(--white);
  }
  .coupon-badge {
    position: absolute; left: 38px; top: 911px; width: 86px; height: 86px;
    border-radius: 50%; background: var(--red); color: var(--white);
    font-family: "Montserrat", Arial, sans-serif; font-weight: 600;
    display: flex; flex-direction: column; align-items: center; justify-content: center; line-height: 1;
  }
  .coupon-badge .big { font-size: 22px; }
  .coupon-badge .small { font-size: 14px; margin-top: 2px; }
  .coupon-text { position: absolute; left: 143px; top: 930px; color: var(--ink); }
  .coupon-text h3 { font-family: "Montserrat", Arial, sans-serif; font-weight: 700; font-size: 20px; letter-spacing: .3px; }
  .coupon-text p { font-size: 19px; margin-top: 2px; }

  .section-title {
    font-family: "Montserrat", Arial, sans-serif; font-weight: 700; font-size: 22px; color: var(--white);
  }
  .guarantee-title { top: 233px; }
  .guarantee-body { top: 272px; font-size: 14px; line-height: 14.5px; }
  .expect-title { top: 358px; }
  .expect-list { top: 396px; font-size: 14px; line-height: 14.5px; list-style: none; }
  .expect-list li { margin-bottom: 14px; }

  .prices {
    position: absolute; left: 41px; top: 582px; width: 289px; height: 286px;
    border: 1.5px solid var(--white); color: var(--white); padding: 14px 18px 0 18px;
    font-size: 10.5px; line-height: 11.5px;
  }
  .prices h4 { font-family: "Montserrat", Arial, sans-serif; font-weight: 700; font-size: 23px; line-height: 22px; }
  .prices .note { font-weight: 700; margin-bottom: 10px; }
  .prices h5 { font-size: 10.5px; font-weight: 700; }
  .prices ul { list-style: none; margin-bottom: 12px; }
  .prices li { position: relative; padding-left: 14px; }
  .prices li::before { content: ""; position: absolute; left: 1px; top: 3px; width: 6px; height: 6px; background: var(--white); }
  .prices b { font-weight: 700; }

  .start-title {
    position: absolute; left: 31px; top: 913px; font-family: "Montserrat", Arial, sans-serif;
    font-weight: 600; font-size: 18px; color: var(--ink);
  }
  .start-contact { position: absolute; left: 32px; top: 946px; color: var(--red); font-size: 8.5px; line-height: 10.5px; }
  .start-contact .name, .start-contact .web { font-weight: 700; }
</style>
</head>
<body>

<section class="hanger hanger--front">
  <div class="panel">
    <div class="photo photo--family" role="img" aria-label="Family playing with balloons on a green lawn in front of trees"></div>
    <div class="hole"></div>
    <p class="center headline msg-1">We mowed<br>your neighbor's lawn<br>today!</p>
    <p class="center headline msg-2">We are<br>in your neighborhood<br>every Tuesday!</p>
    <p class="center headline msg-3">Our lawn service<br>is guaranteed.</p>
    <div class="cta">CALL US TODAY! 512-748-3091</div>
    <div class="center contact">
      <div class="name">VerdaTurf</div>
      <div>P. O. Box 2187, Cedar Park, TX 78613</div>
      <div>Telephone: 512.748.3091 | Fax: 512.748.3092</div>
      <div>Email: hello@verdaturf-example.net</div>
      <div class="web">www.verdaturf-example.net</div>
    </div>
  </div>
  <div class="tearline"></div>
  <div class="coupon-badge"><span class="big">FREE</span><span class="small">COUPON</span></div>
  <div class="coupon-text">
    <h3>GET YOUR COUPON</h3>
    <p>10th Lawn Service Free!</p>
  </div>
</section>

<section class="hanger hanger--back">
  <div class="panel">
    <div class="photo photo--lawn" role="img" aria-label="Hand resting on freshly cut green grass"></div>
    <div class="hole"></div>
    <h2 class="center section-title guarantee-title">Guaranteed Services!</h2>
    <p class="center guarantee-body">That's right! Our services are Guaranteed!<br>Our Guarantee is very simple -<br>If you are not satisfied with the work performed,<br>Our crew will come back and make it right!</p>
    <h2 class="center section-title expect-title">What You Can Expect</h2>
    <ul class="center expect-list">
      <li>Very Responsive staff - same business day<br>responses to you.</li>
      <li>Service on the same day each week.</li>
      <li>Uniformed staff in clean indentifiable trucks.</li>
      <li>Lawn mowed in a different direction each week<br>with blades sharpened daily.</li>
      <li>Very competitive prices.</li>
    </ul>
    <div class="prices">
      <h4>PRICES</h4>
      <p class="note">Lawn Care Prices are based on the gross square footage of your property.</p>
      <h5>Weekly Lawn Care Service Prices<br>(minimum 5 services)</h5>
      <ul>
        <li>Interior Lots &lt; 5,500 Square Feet <b>$24.50</b></li>
        <li>Interior Lots 5,501 to 11,000 Square Feet <b>$27.50</b></li>
        <li>Corner Lot or Cul-de-sac Lot<br>&lt; 5,500 Square Feet <b>$29.50</b></li>
        <li>Corner Lot or Cul-de-sac Lot 5,501 to 11,000 Square Feet <b>$32.50</b></li>
      </ul>
      <h5>Bi-Weekly Lawn Care Service Prices<br>(minimum 5 services)</h5>
      <ul>
        <li>Interior Lots &lt; 5,500 Square Feet <b>$31.50</b></li>
        <li>Interior Lots 5,501 to 11,000 Square Feet <b>$34.50</b></li>
        <li>Corner Lot or Cul-de-sac Lot<br>&lt; 5,500 Square Feet <b>$36.50</b></li>
        <li>Corner Lot or Cul-de-sac Lot 5,501 to 11,000 Square Feet <b>$39.50</b></li>
      </ul>
    </div>
  </div>
  <div class="tearline"></div>
  <h3 class="start-title">Let’s get your lawn care started!</h3>
  <div class="start-contact">
    <div class="name">VerdaTurf</div>
    <div>P. O. Box 2187, Cedar Park, TX 78613</div>
    <div>Telephone: 512.748.3091 | Fax: 512.748.3092 | Email: hello@verdaturf-example.net</div>
    <div class="web">www.verdaturf-example.net</div>
  </div>
</section>

</body>
</html>
```